Social Media Post – Promotion Announcement for Rick Hollis

Objective:
Create a professional and eye-catching social media post announcing the promotion of Rick Hollis to Vice President of Sales – Foodservice. The design should be modern, clean, and aligned with Danbury Sales & Marketing’s branding style (friendly, West Coast, professional). It should match our website:

www.danburysales.example

Key Requirements:

Include Rick Hollis’s photo (we will provide a high-resolution image).
Prominently display his name: “Rick Hollis.”
Prominently display his new title: “Vice President of Sales – Foodservice.”

A header or highlight that says something like: “Promotion Announcement” or “Congratulations!”

Design must be editable in Canva so we can reuse the template for future promotions.

Square format (1080x1080px) for Instagram/LinkedIn, but adaptable to landscape (1200x628px) if possible.

Style Guide / Preferences:

Colors: Incorporate Danbury Sales & Marketing brand blue (#0B64C0) along with white, gray, and/or complementary tones.

Fonts: Clean, modern sans-serif. Readable even on mobile.

Layout: Balanced between photo and text.

Option 1: Circular frame for the photo at center/top, text below.

Option 2: Split design with photo on one side and text on the other.

Tone: Professional, celebratory, approachable.

Deliverables:

Canva template file (editable).

Exported PNG/JPEG preview for review.

```html
<!DOCTYPE html>
<html lang="en">
<head>
<meta charset="utf-8">
<title>Promotion Announcement – Rick Hollis</title>
<link rel="stylesheet" href="https://fonts.googleapis.com/css2?family=Poppins:wght@600;700;800&display=swap">
<style>
  :root {
    --brand-blue: #3A55A7;
    --brand-blue-deep: #3751A4;
    --accent-yellow: #FFC20E;
    --ring-white: #FFFFFF;
    --title-gray: #C3C3C3;
    --photo-yellow: #FEC111;
    --photo-yellow-soft: #F8BC12;
  }
  * { margin: 0; padding: 0; box-sizing: border-box; }
  html, body {
    width: 1200px;
    height: 1200px;
    overflow: hidden;
  }
  body {
    font-family: "Poppins", Arial, sans-serif;
  }
  .post {
    position: relative;
    width: 1200px;
    height: 1200px;
    overflow: hidden;
    background: linear-gradient(180deg,
      var(--brand-blue-deep) 0%,
      var(--brand-blue) 18%,
      #7E8FC7 45%,
      #C9D0E8 68%,
      #FFFFFF 82%,
      #FFFFFF 100%);
  }
  .headline {
    position: absolute;
    top: 40px;
    left: 0;
    width: 100%;
    text-align: center;
    font-weight: 800;
    font-size: 86px;
    line-height: 1;
    letter-spacing: 1px;
    color: var(--accent-yellow);
  }
  .portrait {
    position: absolute;
    left: 258px;
    top: 138px;
    width: 684px;
    height: 684px;
  }
  .portrait svg { display: block; width: 100%; height: 100%; }
  .name {
    position: absolute;
    top: 852px;
    left: 0;
    width: 100%;
    text-align: center;
    font-weight: 700;
    font-size: 158px;
    line-height: 1;
    letter-spacing: 2px;
    color: var(--brand-blue);
    white-space: nowrap;
  }
  .role {
    position: absolute;
    top: 996px;
    left: 0;
    width: 100%;
    text-align: center;
    font-weight: 600;
    font-size: 52px;
    line-height: 1;
    color: var(--title-gray);
    white-space: nowrap;
  }
  .company {
    position: absolute;
    top: 1100px;
    left: 0;
    width: 100%;
    text-align: center;
    font-weight: 700;
    font-size: 32px;
    line-height: 1.1;
    color: var(--brand-blue);
  }
</style>
</head>
<body>
  <main class="post">
    <h1 class="headline">CONGRATULATIONS!</h1>

    <figure class="portrait">
      <svg viewBox="0 0 684 684" xmlns="http://www.w3.org/2000/svg">
        <defs>
          <radialGradient id="portrait-fill" cx="50%" cy="45%" r="60%">
            <stop offset="0%" stop-color="var(--photo-yellow)"/>
            <stop offset="100%" stop-color="var(--photo-yellow-soft)"/>
          </radialGradient>
        </defs>
        <circle class="portrait-ring" cx="342" cy="342" r="342" fill="var(--ring-white)"/>
        <circle class="portrait-photo" cx="342" cy="342" r="310" fill="url(#portrait-fill)"
                role="img" aria-label="Headshot of Rick Hollis in a brown blazer and checked shirt on a yellow background"/>
      </svg>
    </figure>

    <h2 class="name">RICK HOLLIS</h2>
    <p class="role">Vice President of Sales – Foodservice</p>
    <p class="company">Danbury Sales &amp; Marketing</p>
  </main>
</body>
</html>
```